Heron Home Inspections website

I need a website for a new company called Heron Home Inspections, LLC. based in Northern Virginia. I'd like the site built on the url heroninspections.com and incorporating the graphics that I attached.

Project Deadline Extended
Reason: I got bogged down with my job, with a daughter moving, and with two daughters who are in their final stages of pregnancy. I started this web design job at a really bad time in my life. I do appreciate all of the hard work that the designers have put forth and I will soon make my selection. Thank you, Tim

Target Market(s)

Clarke County, Loudoun County, Fairfax County, Fairfax City, Fauquier County, Arlington County, Arlington City, Frederick County, Shenandoah County

Industry/Entity Type

Home Inspection

Number of Pages Required

1 page

Font styles to use
Sans Serif

Requirements
Must have
• My logo
• Company name: Heron Home Inspections, LLC.
• Tim Rudge, Jr.
• Owner / Principal Inspector
• 703-555-0142
• tim.heroninspections@mailvale.com
• A space to describe me and my business
Should not have
• Please use the color scheme of the uploads that I provided

```html
<!DOCTYPE html>
<html lang="en">
<head>
<meta charset="utf-8">
<title>Heron Home Inspections, LLC.</title>
<link rel="stylesheet" href="https://fonts.googleapis.com/css2?family=Raleway:wght@300;400;600;700&family=Open+Sans:wght@400;600;700&display=swap">
<style>
:root{
  --blue:#2b9fd9;
  --blue-dark:#1a7fb6;
  --navy:#1d3d72;
  --ink:#333;
  --muted:#555;
  --pale:#efefef;
  --footer:#2c2c2c;
  --footer-bottom:#1d1d1d;
  --btn:#4a4a4a;
  --white:#fff;
}
*{box-sizing:border-box;margin:0;padding:0}
html,body{width:760px;height:1200px;overflow:hidden;background:var(--white)}
body{font-family:"Open Sans",Arial,sans-serif;color:var(--ink);position:relative}

/* top bar */
.topbar{position:absolute;top:0;left:0;width:760px;height:22px;border-bottom:1px solid #d9d9d9}
.topbar-contacts{position:absolute;right:120px;top:0;height:22px;display:flex;border-left:1px solid #d9d9d9}
.topbar-item{display:flex;align-items:center;gap:5px;padding:0 8px;font-size:9.5px;color:var(--navy);border-right:1px solid #d9d9d9;background:#f6f6f6}
.topbar-item svg{width:10px;height:10px}

/* header */
.header{position:absolute;top:22px;left:0;width:760px;height:64px;border-top:2px solid #e3e3e3}
.brand{position:absolute;left:120px;top:8px;display:flex;align-items:center;gap:6px}
.brand-dot{width:20px;height:20px;border-radius:50%;background:var(--blue)}
.brand-name{font-family:"Raleway",sans-serif;font-weight:700;font-size:13px;line-height:14px;color:var(--navy)}
.search{position:absolute;left:486px;top:14px;width:155px;height:16px;display:flex;border:1px solid #cfcfcf;border-radius:2px}
.search-field{flex:1;font-size:6.5px;color:#888;padding:3px 5px}
.search-btn{width:24px;background:var(--blue);display:flex;align-items:center;justify-content:center}
.nav{position:absolute;left:265px;top:42px;display:flex;gap:13px;font-size:9.5px;text-transform:uppercase;color:#444}
.nav a{color:inherit;text-decoration:none;padding-bottom:5px}
.nav a.active{color:var(--blue);border-bottom:2px solid var(--blue)}

/* hero */
.hero{position:absolute;top:86px;left:0;width:760px;height:298px;
  background:radial-gradient(ellipse at 40% 35%,#d9a64f 0%,#9b6a2d 35%,#5a3417 70%,#3a2010 100%)}
.hero-title{position:absolute;top:104px;width:100%;text-align:center;font-family:"Raleway",sans-serif;font-weight:700;font-size:29px;color:var(--white);text-shadow:0 1px 3px rgba(0,0,0,.45)}
.hero-sub{position:absolute;top:140px;width:100%;text-align:center;font-family:"Raleway",sans-serif;font-weight:400;font-size:19.5px;color:var(--white);text-shadow:0 1px 3px rgba(0,0,0,.45)}
.hero-btn{position:absolute;top:176px;left:340px;width:80px;height:22px;border:2px solid var(--white);border-radius:12px;font-family:"Raleway",sans-serif;font-weight:700;font-size:11px;color:var(--white);text-align:center;line-height:18px}
.hero-arrow{position:absolute;top:134px}
.hero-dots{position:absolute;top:288px;left:361px;display:flex;gap:3px}
.dot{width:6px;height:6px;border-radius:50%;border:1px solid #bbb;background:var(--white)}
.dot.on{background:var(--blue);border-color:var(--blue)}

.section-title{position:absolute;width:100%;text-align:center;font-family:"Raleway",sans-serif;font-weight:400;font-size:21px;color:var(--blue)}

/* services */
.services{position:absolute;top:384px;left:0;width:760px;height:242px;background:var(--white)}
.service{position:absolute;top:60px;width:164px;text-align:center}
.service-icon{width:76px;height:76px;margin:0 auto;border-radius:50%;border:2px solid #444;padding:3px}
.service-icon-inner{width:100%;height:100%;border-radius:50%;background:var(--blue);display:flex;align-items:center;justify-content:center}
.service-name{margin-top:8px;font-family:"Raleway",sans-serif;font-size:12.5px;color:var(--blue)}
.service-text{margin-top:4px;font-size:7.6px;line-height:10.5px;color:#222;font-weight:400}
.btn-more{display:inline-block;margin-top:8px;width:66px;height:16px;border-radius:2px;background:var(--btn);color:var(--white);font-size:7.5px;font-weight:700;line-height:16px}

/* about */
.about{position:absolute;top:626px;left:0;width:760px;height:224px;background:var(--pale);overflow:hidden}
.about-photo{position:absolute;left:171px;top:66px;width:66px;height:66px;border-radius:50%;background:linear-gradient(160deg,#c9b8a3,#6f5a4a)}
.about-card{position:absolute;left:120px;top:140px;width:168px;text-align:center;font-size:8.5px;line-height:15px;font-weight:700;color:#222}
.about-card .name{color:var(--blue);font-weight:600}
.about-body{position:absolute;left:293px;top:52px;width:350px;font-size:7.8px;line-height:11.2px;color:#333}
.about-body p{margin-bottom:7px}
.about-body h3{font-size:8px;font-weight:700;color:var(--blue);margin-bottom:6px}
.about-body .hl{color:var(--blue)}

/* testimonials */
.testimonials{position:absolute;top:850px;left:0;width:760px;height:182px;background:var(--white)}
.t-photo{position:absolute;left:160px;top:45px;width:76px;height:76px;border-radius:50%;border:3px solid var(--blue);background:linear-gradient(160deg,#d7c2ad,#2c3850)}
.t-stars{position:absolute;left:160px;top:126px;width:76px;text-align:center;font-size:8px;color:#f2b01e;letter-spacing:1px}
.t-name{position:absolute;left:140px;top:137px;width:116px;text-align:center;font-size:7px;font-weight:700;color:var(--blue)}
.t-role{position:absolute;left:140px;top:149px;width:116px;text-align:center;font-size:6.5px;color:#444}
.t-text{position:absolute;left:252px;top:58px;width:350px;text-align:center;font-size:6.6px;line-height:12px;color:#333}
.t-arrow{position:absolute;top:92px}
.t-dots{position:absolute;left:553px;top:125px;display:flex;gap:3px}

/* footer */
.footer{position:absolute;top:1032px;left:0;width:760px;height:146px;background:var(--footer)}
.f-col{position:absolute;top:26px}
.f-head{font-size:8.5px;font-weight:700;color:var(--blue);margin-bottom:7px}
.f-text{font-size:6.4px;line-height:11px;color:#ddd}
.f-text p{margin-bottom:6px}
.f-links{list-style:none;font-size:6.6px;line-height:13px;color:#ddd}
.f-social{display:flex;gap:4px;margin-bottom:10px}
.f-social span{width:12px;height:12px;border-radius:50%;background:#888}
.f-awards{display:flex;gap:6px;align-items:center}
.award-round{width:42px;height:42px;border-radius:50%;background:var(--white);border:3px solid #777}
.award-rect{width:78px;height:36px;border-radius:18px;background:var(--white);border:3px solid #777}
.bottombar{position:absolute;top:1178px;left:0;width:760px;height:22px;background:var(--footer-bottom);font-size:5.8px;color:#ccc}
.bottombar .left{position:absolute;left:119px;top:7px}
.bottombar .right{position:absolute;right:119px;top:7px}
</style>
</head>
<body>

<div class="topbar">
  <div class="topbar-contacts">
    <div class="topbar-item">
      <svg viewBox="0 0 10 10"><rect x="0.5" y="2" width="9" height="6" fill="none" stroke="#1d3d72"/><path d="M0.5 2 L5 5.5 L9.5 2" fill="none" stroke="#1d3d72"/></svg>
      Email: tim.heroninspections@mailvale.com
    </div>
    <div class="topbar-item">
      <svg viewBox="0 0 10 10"><path d="M2 1 L4 1 L4.8 3.2 L3.6 4.2 Q4.6 6 6 6.6 L7 5.4 L9 6.2 L9 8.2 Q5 9 1.8 4.6 Q1 3 2 1Z" fill="#1d3d72"/></svg>
      Call us: 703-555-0142
    </div>
  </div>
</div>

<header class="header">
  <div class="brand">
    <span class="brand-dot"></span>
    <div class="brand-name">Heron<br>Home Inspections, LLC.</div>
  </div>
  <div class="search">
    <div class="search-field">type to search ...</div>
    <div class="search-btn">
      <svg width="9" height="9" viewBox="0 0 10 10"><circle cx="4" cy="4" r="3" fill="none" stroke="#fff" stroke-width="1.4"/><path d="M6.2 6.2 L9 9" stroke="#fff" stroke-width="1.6"/></svg>
    </div>
  </div>
  <nav class="nav">
    <a class="active">Home</a><a>About Us</a><a>Inspection Services</a><a>Inspection Requests</a><a>Contact Us</a>
  </nav>
</header>

<section class="hero" role="img" aria-label="Photo of a warmly lit hotel bedroom with bed, lamps and patterned carpet">
  <svg class="hero-arrow" style="left:6px" width="14" height="26" viewBox="0 0 14 26"><path d="M12 2 L3 13 L12 24" fill="none" stroke="rgba(255,255,255,.7)" stroke-width="3"/></svg>
  <svg class="hero-arrow" style="right:6px" width="14" height="26" viewBox="0 0 14 26"><path d="M2 2 L11 13 L2 24" fill="none" stroke="rgba(255,255,255,.7)" stroke-width="3"/></svg>
  <h1 class="hero-title">YOUR SUCCESS IN PROPERTY OPERATIONS</h1>
  <p class="hero-sub">Services for commercial, industrial and residential properties</p>
  <div class="hero-btn">Get Started</div>
  <div class="hero-dots"><span class="dot"></span><span class="dot"></span><span class="dot on"></span><span class="dot"></span><span class="dot"></span></div>
</section>

<section class="services">
  <h2 class="section-title" style="top:18px">Our Services</h2>
  <div class="service" style="left:123px">
    <div class="service-icon"><div class="service-icon-inner">
      <svg width="30" height="28" viewBox="0 0 30 28"><rect x="4" y="6" width="22" height="22" fill="#fff"/><g fill="#2b9fd9"><rect x="8" y="10" width="3" height="3"/><rect x="13.5" y="10" width="3" height="3"/><rect x="19" y="10" width="3" height="3"/><rect x="8" y="16" width="3" height="3"/><rect x="13.5" y="16" width="3" height="3"/><rect x="19" y="16" width="3" height="3"/><rect x="13" y="22" width="4" height="6"/></g></svg>
    </div></div>
    <div class="service-name">Commercial</div>
    <p class="service-text">Lorem ipsum dolor sit amet, consectetur adipisicing elit, sed do eiusmod teml abore et dolore magna aliqua.</p>
    <span class="btn-more">Learn More</span>
  </div>
  <div class="service" style="left:298px">
    <div class="service-icon"><div class="service-icon-inner">
      <svg width="30" height="30" viewBox="0 0 30 30"><path d="M6 28 L6 8 L15 2 L15 28Z" fill="#fff"/><path d="M16 28 L16 6 L24 10 L24 28Z" fill="#e8f4fb"/><g stroke="#2b9fd9" stroke-width="1"><path d="M8 12 H13 M8 16 H13 M8 20 H13 M18 14 H22 M18 18 H22 M18 22 H22"/></g></svg>
    </div></div>
    <div class="service-name">Industrial</div>
    <p class="service-text">Lorem ipsum dolor sit amet, consectetur adipisicing elit, sed do eiusmod teml abore et dolore magna aliqua.</p>
    <span class="btn-more">Learn More</span>
  </div>
  <div class="service" style="left:473px">
    <div class="service-icon"><div class="service-icon-inner">
      <svg width="30" height="30" viewBox="0 0 30 30"><rect x="6" y="4" width="12" height="24" fill="#fff"/><rect x="18" y="12" width="7" height="16" fill="#e8f4fb"/><g fill="#2b9fd9"><rect x="9" y="8" width="2.5" height="2.5"/><rect x="13" y="8" width="2.5" height="2.5"/><rect x="9" y="13" width="2.5" height="2.5"/><rect x="13" y="13" width="2.5" height="2.5"/><rect x="9" y="18" width="2.5" height="2.5"/><rect x="13" y="18" width="2.5" height="2.5"/><rect x="20" y="16" width="3" height="2.5"/><rect x="20" y="21" width="3" height="2.5"/></g></svg>
    </div></div>
    <div class="service-name">Residential</div>
    <p class="service-text">Lorem ipsum dolor sit amet, consectetur adipisicing elit, sed do eiusmod teml abore et dolore magna aliqua.</p>
    <span class="btn-more">Learn More</span>
  </div>
</section>

<section class="about">
  <h2 class="section-title" style="top:14px">About us</h2>
  <div class="about-photo" role="img" aria-label="Portrait photo of the owner, Tim Rudge, Jr."></div>
  <div class="about-card">
    <div class="name">Tim Rudge, Jr.</div>
    <div>CEO, Heron Home Inspections, LLC.</div>
    <div>tim.heroninspections@mailvale.com</div>
    <div>Call Me : 703-555-0142</div>
  </div>
  <div class="about-body">
    <p>Owner, <span class="hl">Tim Rudge</span> is a trained builder with experience in new construction, as well as remodeling, HVAC systems, framing, roofing, siding, and masonry</p>
    <h3>Why get a Home Inspection</h3>
    <p>For most families, a home purchase is the largest investment that they will make in a lifetime. The decision to purchase a home should be based on a thorough review of its systems and overall condition to ensure that their investment is one based research and fact. A good home inspector will give you the research based facts that help a buyer to make the best possible decision in a home purchase.</p>
    <h3>Why use Heron Inspections</h3>
    <p>I am a 20 year Navy veteran trained and devoted to being thorough in my inspection procedures and comprehensive in my documentation. Whether you are buying your forever home or one that you plan to have for a few years and then move on, protect your investment by knowing what you are buying before you sign.</p>
  </div>
</section>

<section class="testimonials">
  <h2 class="section-title" style="top:20px">Testimonials</h2>
  <svg class="t-arrow" style="left:122px" width="8" height="14" viewBox="0 0 8 14"><path d="M7 1 L1 7 L7 13" fill="none" stroke="#aaa" stroke-width="1.5"/></svg>
  <svg class="t-arrow" style="left:630px" width="8" height="14" viewBox="0 0 8 14"><path d="M1 1 L7 7 L1 13" fill="none" stroke="#aaa" stroke-width="1.5"/></svg>
  <div class="t-photo" role="img" aria-label="Portrait photo of the reviewer"></div>
  <div class="t-stars">★★★★★</div>
  <div class="t-name">Alan Mercer</div>
  <div class="t-role">CTO, Company Name</div>
  <p class="t-text">Lorem ipsum dolor sit amet, consectetur adipisicing elit, sed do eiusmod tempor incididunt ut labore et dolore magna aliqua. Ut enim ad minim veniam, quis nostrud exercitation ullamco laboris nisi ut aliquip ex ea commodo consequat. Duis aute irure dolor in reprehenderit in voluptate velit esse cillum dolore eu fugiat nulla pariatur. Excepteur sint occaecat cupidatat non proident, sunt in culpa qui officia deserunt mollit anim id est laborum. Sed ut perspiciatis.</p>
  <div class="t-dots"><span class="dot"></span><span class="dot"></span><span class="dot on"></span><span class="dot"></span><span class="dot"></span></div>
</section>

<footer class="footer">
  <div class="f-col" style="left:119px;width:130px">
    <div class="f-head">About Us</div>
    <div class="f-text">
      <p>Lorem ipsum dolor sit amet, consectetur adipisicing elit, sed do eiusmod tempor incididunt ut labore et dolore magna aliqua. Ut enim ad minim veniam, quis nostrud.</p>
      <p>Laboris nisi ut aliquip ex ea commodo consequat. Duis aute irure dolor in reprehenderit in voluptate velit esse pariatur.</p>
    </div>
  </div>
  <div class="f-col" style="left:305px">
    <div class="f-head">Quick Links</div>
    <ul class="f-links"><li>Home</li><li>Mission</li><li>About us</li><li>Inspection Services</li><li>Inspection Requests</li><li>Contact us</li></ul>
  </div>
  <div class="f-col" style="left:422px;width:150px">
    <div class="f-head">Stay Connected</div>
    <div class="f-text" style="line-height:12.5px">
      Heron Home Inspections, LLC.<br>Address Street Here, Number here,<br>Area Code here, City, 20190.<br>Email : <span style="color:var(--blue)">contact@heroninspections.com</span><br>Phone : 703-555-0142<br>Fax : 703-555-0199
    </div>
  </div>
  <div class="f-col" style="left:589px">
    <div class="f-head">Social</div>
    <div class="f-social"><span></span><span></span><span></span></div>
    <div class="f-head">Awards</div>
    <div class="f-awards"><div class="award-round"></div><div class="award-rect"></div></div>
  </div>
</footer>
<div class="bottombar">
  <span class="left">Copyright 2014 - 2015 | Sitemap</span>
  <span class="right">Privacy Policy | Terms &amp; Conditions | Cookie Policy</span>
</div>

</body>
</html>
```